Construction business card

I need a new business card, they can connect with my logo, brand.
What we do is residential house , design and build
I like: Navy blue / black
I attached our logo, brand,
and, some idea for business card.

```html
<!DOCTYPE html>
<html lang="en">
<head>
<meta charset="utf-8">
<title>Ridgeline Build Co – Business Card</title>
<link href="https://fonts.googleapis.com/css2?family=Arimo:wght@400;700&display=swap" rel="stylesheet">
<style>
  :root {
    --bg-top: #d4d4d4;
    --bg-bottom: #9c9c9c;
    --card: #2b2c2e;
    --card-deco: #333436;
    --edge: #3a86d0;
    --accent: #3f8fdc;
    --ink: #ffffff;
    --muted: #e6e6e6;
  }
  * { margin: 0; padding: 0; box-sizing: border-box; }
  html, body { width: 1200px; height: 802px; overflow: hidden; }
  body {
    background: linear-gradient(180deg, var(--bg-top), var(--bg-bottom));
    font-family: "Arimo", Arial, sans-serif;
    display: flex;
    align-items: center;
    justify-content: center;
    gap: 60px;
  }
  .card {
    position: relative;
    width: 520px;
    height: 300px;
    background: var(--card);
    border-radius: 22px;
    border-bottom: 5px solid var(--edge);
    box-shadow: 0 18px 30px rgba(0,0,0,0.35);
    overflow: hidden;
  }
  /* Front side */
  .card-front__deco {
    position: absolute;
    right: 40px;
    top: 40px;
    font-weight: 700;
    font-size: 92px;
    letter-spacing: 2px;
    color: var(--card-deco);
    line-height: 1;
  }
  .contact {
    position: absolute;
    left: 40px;
    top: 78px;
    color: var(--muted);
  }
  .contact__name {
    color: var(--accent);
    font-weight: 700;
    font-size: 22px;
  }
  .contact__role {
    font-size: 13px;
    margin-top: 2px;
  }
  .contact__address {
    font-size: 13px;
    line-height: 1.35;
    margin-top: 34px;
  }
  .contact__list {
    list-style: none;
    margin-top: 8px;
    font-size: 13px;
  }
  .contact__list li {
    display: flex;
    align-items: center;
    gap: 8px;
    line-height: 1.55;
  }
  .contact__list svg { width: 11px; height: 11px; fill: var(--accent); flex: none; }
  .tagline {
    position: absolute;
    right: 36px;
    bottom: 28px;
    font-weight: 700;
    font-size: 15px;
    color: var(--ink);
  }
  .tagline span { color: var(--accent); }
  /* Back side */
  .card-back {
    display: flex;
    align-items: center;
    justify-content: center;
    gap: 12px;
  }
  .brand__mark {
    width: 16px;
    height: 16px;
    background: var(--accent);
  }
  .brand__name {
    font-weight: 700;
    font-size: 30px;
    letter-spacing: 1px;
    color: var(--ink);
    text-transform: uppercase;
  }
</style>
</head>
<body>
  <article class="card card-front">
    <div class="card-front__deco" aria-hidden="true">RIDGELINE</div>
    <div class="contact">
      <h1 class="contact__name">Dalen Ashworth</h1>
      <p class="contact__role">Director</p>
      <p class="contact__address">48 Ferngate St,<br>Oakvale, VIC 3190</p>
      <ul class="contact__list">
        <li><svg viewBox="0 0 24 24"><path d="M6.6 10.8a15.1 15.1 0 0 0 6.6 6.6l2.2-2.2c.3-.3.7-.4 1-.2 1.1.4 2.3.6 3.6.6.6 0 1 .4 1 1V20c0 .6-.4 1-1 1A17 17 0 0 1 3 4c0-.6.4-1 1-1h3.5c.6 0 1 .4 1 1 0 1.3.2 2.5.6 3.6.1.3 0 .7-.2 1z"/></svg>0400 555 018</li>
        <li><svg viewBox="0 0 24 24"><path d="M2 5h20v14H2zm2 2v.5l8 5 8-5V7z"/></svg>hello@ridgelinebuild.com.au</li>
        <li><svg viewBox="0 0 24 24"><circle cx="12" cy="12" r="10"/></svg>ridgelinebuild.com.au</li>
      </ul>
    </div>
    <p class="tagline">Design and <span>Build</span></p>
  </article>

  <article class="card card-back">
    <span class="brand__mark" aria-hidden="true"></span>
    <span class="brand__name">Ridgeline Build Co</span>
  </article>
</body>
</html>
```